Business Card Design

Lawn service

Industry/Entity Type

Business

Contact Information for Business Card

Fernway Turf & Garden , marla dunwick/owner,operater,2146 hollister creekrd.. w. larkmoor,tn. 37999, phone:555-274-0963, Residential,Commercial, Lawn and Landscape Maintenance, Bushhogging

```html
<!DOCTYPE html>
<html lang="en">
<head>
<meta charset="utf-8">
<title>Fernway Turf &amp; Garden — Business Card</title>
<link rel="stylesheet" href="https://fonts.googleapis.com/css2?family=Questrial&display=swap">
<style>
  :root {
    --brand-blue: #17a3d4;
    --ink: #1e1e1e;
    --paper: #ffffff;
    --backdrop: #e9eaeb;
    --card-shadow: rgba(0, 0, 0, 0.18);
  }
  html, body {
    margin: 0;
    padding: 0;
    width: 1200px;
    height: 1000px;
    overflow: hidden;
    background: var(--backdrop);
    font-family: "Questrial", "Helvetica Neue", Arial, sans-serif;
  }
  .business-card {
    position: absolute;
    left: 150px;
    top: 240px;
    width: 900px;
    height: 520px;
    background: var(--paper);
    border-radius: 36px;
    overflow: hidden;
    box-shadow: 0 12px 30px var(--card-shadow);
  }
  .brand {
    position: absolute;
    left: 60px;
    top: 210px;
    width: 340px;
    color: var(--ink);
  }
  .brand-name {
    margin: 0;
    font-size: 38px;
    font-weight: 400;
    letter-spacing: 3px;
    line-height: 1.2;
    white-space: nowrap;
  }
  .divider {
    position: absolute;
    left: 420px;
    top: 70px;
    width: 2px;
    height: 300px;
    background: linear-gradient(to bottom, rgba(23,163,212,0), var(--brand-blue) 45%, rgba(23,163,212,0));
  }
  .contact {
    position: absolute;
    right: 50px;
    top: 44px;
    width: 410px;
    text-align: right;
  }
  .contact-name {
    margin: 0;
    color: var(--brand-blue);
    font-size: 26px;
    letter-spacing: 1px;
  }
  .contact-role {
    margin: 2px 0 0;
    color: var(--ink);
    font-size: 22px;
    letter-spacing: 1px;
  }
  .contact-lines {
    list-style: none;
    margin: 54px 0 0;
    padding: 0;
  }
  .contact-line {
    display: flex;
    justify-content: flex-end;
    align-items: flex-start;
    gap: 12px;
    color: var(--brand-blue);
    font-size: 23px;
    letter-spacing: 1px;
    line-height: 1.25;
    margin-bottom: 10px;
    white-space: nowrap;
  }
  .contact-icon {
    flex: 0 0 auto;
    width: 30px;
    height: 30px;
  }
  .services-band {
    position: absolute;
    left: 0;
    bottom: 0;
    width: 100%;
    height: 108px;
    background: var(--brand-blue);
    display: flex;
    align-items: center;
    justify-content: center;
  }
  .services {
    margin: 0;
    color: var(--paper);
    font-size: 25px;
    letter-spacing: 0.5px;
    white-space: nowrap;
  }
</style>
</head>
<body>
  <article class="business-card">
    <header class="brand">
      <h1 class="brand-name">Fernway<br>Turf &amp; Garden</h1>
    </header>

    <div class="divider"></div>

    <section class="contact">
      <p class="contact-name">Marla Dunwick</p>
      <p class="contact-role">owner/operater</p>
      <ul class="contact-lines">
        <li class="contact-line">
          <span>555-274-0963</span>
          <svg class="contact-icon" viewBox="0 0 34 34" aria-hidden="true">
            <path d="M17 2 L32 12 L32 32 L2 32 L2 12 Z" fill="var(--brand-blue)"/>
            <path d="M12 13c1-1 2-1 2.5 0l1.5 2.5c.4.7 0 1.3-.6 1.7 .8 1.8 2 3 3.7 3.8.4-.6 1-1 1.7-.6l2.5 1.5c1 .5 1 1.5 0 2.5-1.5 1.5-4 1-7-1.7s-4.2-5.6-4.3-7.7z" fill="#fff"/>
          </svg>
        </li>
        <li class="contact-line">
          <span>2146 hollister creekrd. w.<br>larkmoor,tn.<br>37999</span>
          <svg class="contact-icon" viewBox="0 0 34 34" aria-hidden="true">
            <path d="M17 2 L32 12 L32 32 L2 32 L2 12 Z" fill="var(--brand-blue)"/>
            <path d="M17 11a5.5 5.5 0 0 1 5.5 5.5c0 4-5.5 10-5.5 10s-5.5-6-5.5-10A5.5 5.5 0 0 1 17 11z" fill="#fff"/>
            <circle cx="17" cy="16.5" r="2" fill="var(--brand-blue)"/>
          </svg>
        </li>
      </ul>
    </section>

    <footer class="services-band">
      <p class="services">Residential,Commercial, Lawn &amp; Landscape Maintenance, Bushhogging</p>
    </footer>
  </article>
</body>
</html>
```